Fun relaxed Travel Photography Business Card*

Require a fun, funky and quirky but rememberable business card for a travel photographer

Industry/Entity Type

Photographer

Contact Information for Business Card

Front Card

(my name) Tavo M.

Travel Photographer ( small under travel photographer) “self-proclaimed”

(website logo) wanderingtavo.example

(Instagram logo) @wandering_with_tavo

(Instagram logo) @wandering_with_tavo_2.0 (backup for when Instagram puts Tavo on timeout for bad behaviour)

Tel: N/A (removing the potential awkwardness of me not replying)

Email: (see above)

Back Card

Offending people since 1986

(Bottom right corner) “p.s. travelling made me fatTER”

Font styles to use
Serif

Colors

Designer to choose colors to be used in the design.

Requirements
Must have
• a camera
• a similar cartoon version of me as the "logo" see attached files, try to make as similar as possible

```html
<!DOCTYPE html>
<html lang="en">
<head>
<meta charset="utf-8">
<title>Tavo M. – Travel Photographer Business Card</title>
<link rel="stylesheet" href="https://fonts.googleapis.com/css2?family=Montserrat:wght@400;500;700&family=Righteous&display=swap">
<style>
  :root {
    --backdrop: #dcdcdc;
    --card-top: #212121;
    --card-bottom: #0c0d0f;
    --accent: #f26522;
    --ink: #ffffff;
    --art-shirt: #3b3f8f;
    --art-flower: #e8742c;
    --art-skin: #5a3320;
    --art-shorts: #d8ccb2;
  }
  html, body {
    margin: 0;
    padding: 0;
    width: 1200px;
    height: 1200px;
    overflow: hidden;
    background: var(--backdrop);
    font-family: "Montserrat", Arial, sans-serif;
  }
  .canvas {
    position: relative;
    width: 1200px;
    height: 1200px;
  }
  .card {
    position: absolute;
    width: 411px;
    background: linear-gradient(180deg, var(--card-top) 0%, var(--card-bottom) 100%);
    overflow: hidden;
    color: var(--ink);
  }
  .card--back { left: 132px; top: 225px; height: 718px; }
  .card--front { left: 649px; top: 227px; height: 716px; }
  .card__band {
    position: absolute;
    left: 0; right: 0; bottom: 0;
    background: var(--accent);
  }
  .card--back .card__band { height: 45px; }
  .card--front .card__band { height: 39px; }

  .tagline {
    position: absolute;
    top: 106px;
    left: 0; right: 0;
    text-align: center;
    font-family: "Righteous", "Arial Black", sans-serif;
    font-size: 28px;
    line-height: 35px;
    letter-spacing: 1px;
    text-transform: uppercase;
    color: transparent;
    -webkit-text-stroke: 1.3px var(--ink);
    margin: 0;
  }
  .postscript {
    position: absolute;
    top: 632px;
    left: 0; right: 0;
    text-align: center;
    font-size: 17px;
    margin: 0;
  }
  .postscript strong { font-weight: 700; }

  .mascot {
    position: absolute;
    border-radius: 6px;
  }
  .mascot--legs {
    left: 173px; top: 262px; width: 238px; height: 162px;
    background: linear-gradient(90deg, var(--art-skin) 0%, var(--art-skin) 45%, var(--art-shorts) 55%, var(--art-shorts) 75%, var(--art-shirt) 85%, var(--art-flower) 100%);
    opacity: 0.85;
  }
  .mascot--torso {
    left: 0; top: 235px; width: 306px; height: 180px;
    background: linear-gradient(90deg, var(--art-shirt) 0%, var(--art-flower) 25%, var(--art-shirt) 45%, var(--art-skin) 65%, var(--art-skin) 100%);
    opacity: 0.85;
  }

  .identity {
    position: absolute;
    top: 80px;
    left: 0; right: 0;
    text-align: center;
    text-transform: uppercase;
  }
  .identity__name {
    margin: 0;
    color: var(--accent);
    font-size: 28px;
    font-weight: 500;
    line-height: 34px;
  }
  .identity__role {
    margin: 0;
    font-size: 17px;
    font-weight: 500;
    line-height: 22px;
  }
  .identity__note {
    margin: 0;
    font-size: 14px;
    line-height: 20px;
  }

  .contacts {
    position: absolute;
    left: 47px;
    top: 472px;
    margin: 0;
    padding: 0;
    list-style: none;
  }
  .contact {
    position: absolute;
    left: 0;
    display: flex;
    align-items: center;
    width: 320px;
    font-size: 17px;
    line-height: 21px;
  }
  .contact__icon {
    width: 32px; height: 32px;
    flex: none;
    margin-right: 18px;
  }
  .contact--web { top: 0; }
  .contact--social { top: 46px; }
  .contact--phone { top: 106px; }
  .contact--mail { top: 152px; }
</style>
</head>
<body>
<main class="canvas">

  <section class="card card--back" aria-label="Card back">
    <h2 class="tagline">Offending people<br>since 1986</h2>
    <div class="mascot mascot--legs" role="img" aria-label="Cartoon mascot’s legs in shorts and sandals, continuing onto the other card"></div>
    <p class="postscript">p.s. travelling made me fat<strong>TER</strong></p>
    <div class="card__band"></div>
  </section>

  <section class="card card--front" aria-label="Card front">
    <header class="identity">
      <h1 class="identity__name">Tavo M.</h1>
      <p class="identity__role">Travel Photographer</p>
      <p class="identity__note">(Self-proclaimed)</p>
    </header>
    <div class="mascot mascot--torso" role="img" aria-label="Cartoon mascot in floral shirt and sunglasses, continuing from the other card"></div>

    <ul class="contacts">
      <li class="contact contact--web">
        <svg class="contact__icon" viewBox="0 0 32 32" aria-hidden="true">
          <circle cx="16" cy="16" r="16" fill="#fff"/>
          <g fill="none" stroke="#111" stroke-width="1.4">
            <circle cx="16" cy="16" r="9"/>
            <ellipse cx="16" cy="16" rx="4" ry="9"/>
            <line x1="7" y1="16" x2="25" y2="16"/>
            <line x1="8.5" y1="11.5" x2="23.5" y2="11.5"/>
            <line x1="8.5" y1="20.5" x2="23.5" y2="20.5"/>
            <line x1="16" y1="7" x2="16" y2="25"/>
          </g>
        </svg>
        <span>wanderingtavo.example</span>
      </li>
      <li class="contact contact--social">
        <svg class="contact__icon" viewBox="0 0 32 32" aria-hidden="true">
          <circle cx="16" cy="16" r="16" fill="#fff"/>
        </svg>
        <span>@wandering_with_tavo<br>@wandering_with_tavo_2.0</span>
      </li>
      <li class="contact contact--phone">
        <svg class="contact__icon" viewBox="0 0 32 32" aria-hidden="true">
          <circle cx="16" cy="16" r="16" fill="#fff"/>
          <path d="M11 8.5c1-.6 2-.2 2.5.8l1.4 2.8c.4.8.1 1.6-.6 2.1l-1 .7c.8 2 2.3 3.6 4.2 4.6l.8-1c.5-.7 1.4-.9 2.1-.5l2.7 1.5c.9.5 1.2 1.6.6 2.5l-1 1.5c-.7 1-2 1.4-3.2 1-5-1.8-8.8-5.8-10.4-10.8-.4-1.2 0-2.5 1-3.2z" fill="#111"/>
        </svg>
        <span>N/A</span>
      </li>
      <li class="contact contact--mail">
        <svg class="contact__icon" viewBox="0 0 32 32" aria-hidden="true">
          <circle cx="16" cy="16" r="16" fill="#fff"/>
          <rect x="7.5" y="10" width="17" height="12" rx="1" fill="none" stroke="#111" stroke-width="1.6"/>
          <path d="M7.5 10.5 16 17l8.5-6.5M7.5 21.5l6-5.5M24.5 21.5l-6-5.5" fill="none" stroke="#111" stroke-width="1.6"/>
        </svg>
        <span>N/A</span>
      </li>
    </ul>
    <div class="card__band"></div>
  </section>

</main>
</body>
</html>
```